Business card for a plastic surgeon

i need a business card for a plastic surgeon. I have two adresses. The card should communicate safety, simmetry, beauty and with soft colors.
What i want in the card:
- my logo: Letters "R"and "B" (picture uploaded)
- my name: Renato Bastiani
- my registration: CRM 507 219
- my adresses and phone numbers (2):
- Av Dr Teixeira Lopes, 2710, sala 305 - Vila Olímpia | São Paulo/ SP - Phone: 11 4172-5036
- Al. Itapeva, 47, 3 andar - Alphaville | Barueri/ SP - Phone: 11 6350-2481

- my social network: site, facebook and instagram

Target Market(s)

people (95% girls and women) that want cosmetic procedures and plastic surgery

Industry/Entity Type

Business

Contact Information for Business Card

The card should communicate safety, simmetry, beauty and with soft colors.
Beige, brown, gray, rosy are some options. Color is free

Font styles to use
Serif

Requirements
Must have
• - my logo: Letters "R"and "B" (picture uploaded)
• - my name: Renato Bastiani
• - my registration: CRM 507 219
• - my adresses and phone numbers (2):
• - Av Dr Teixeira Lopes, 2710, sala 305 - Vila Olímpia | São Paulo/ SP - Phone: 11 4172-5036
• - Al. Itapeva, 47, 3 andar - Alphaville | Barueri/ SP - Phone: 11 6350-2481
• - my social network: site, facebook and instagram
Should not have
• other images (only my logo)

```html
<!DOCTYPE html>
<html lang="pt-BR">
<head>
<meta charset="utf-8">
<title>Renato Bastiani – Cartão de Visita</title>
<link rel="stylesheet" href="https://fonts.googleapis.com/css2?family=Cinzel:wght@400;500&display=swap">
<style>
  :root {
    --bg: #e4e3e1;
    --card: #ffffff;
    --brown: #a28a74;
    --ink: #9a7f68;
    --light: #fbf8f5;
  }
  * { box-sizing: border-box; margin: 0; padding: 0; }
  html, body { width: 1176px; height: 1200px; overflow: hidden; }
  body {
    background: var(--bg);
    font-family: "Cinzel", "Times New Roman", serif;
    color: var(--ink);
    display: flex;
    flex-direction: column;
    align-items: center;
    justify-content: center;
    gap: 60px;
  }
  .card {
    position: relative;
    width: 900px;
    height: 514px;
    border-radius: 42px;
    background: var(--card);
    overflow: hidden;
    box-shadow: 0 10px 30px rgba(0,0,0,0.12);
  }

  /* Front */
  .front .identity {
    position: absolute;
    top: 70px; left: 0; right: 0;
    text-align: center;
  }
  .monogram {
    font-weight: 400;
    color: var(--ink);
    letter-spacing: 0.04em;
  }
  .front .monogram { font-size: 92px; line-height: 1; }
  .name {
    font-weight: 400;
    font-size: 34px;
    letter-spacing: 0.03em;
    line-height: 1.1;
  }
  .specialty {
    font-size: 16px;
    letter-spacing: 0.32em;
    line-height: 1.3;
  }
  .front .name { margin-top: 40px; }
  .front .specialty { margin-top: 4px; }
  .socials {
    position: absolute;
    left: 0; right: 0; bottom: 58px;
    display: flex;
    justify-content: center;
    gap: 56px;
    font-size: 14px;
    letter-spacing: 0.04em;
  }
  .social { display: flex; flex-direction: column; align-items: center; gap: 10px; }
  .social-mark { width: 22px; height: 22px; border: 2px solid var(--ink); }
  .social-mark.square { border-radius: 4px; }
  .social-mark.circle { border-radius: 50%; }

  /* Back */
  .back .header {
    position: absolute;
    top: 48px; left: 56px;
    display: flex;
    align-items: center;
    gap: 18px;
  }
  .back .monogram { font-size: 56px; line-height: 1; }
  .back .name { font-size: 30px; }
  .back .specialty { font-size: 14px; }
  .registration {
    position: absolute;
    top: 168px; right: 62px;
    font-size: 17px;
    letter-spacing: 0.04em;
  }
  .band {
    position: absolute;
    left: 0; right: 0; bottom: 0;
    height: 300px;
    background: var(--brown);
    color: var(--light);
    display: flex;
    flex-direction: column;
    align-items: center;
    justify-content: center;
    gap: 18px;
  }
  .address { text-align: center; font-size: 18px; line-height: 1.45; letter-spacing: 0.02em; }
  .line { display: flex; align-items: center; justify-content: center; gap: 8px; }
  .icon { width: 16px; height: 16px; fill: none; stroke: var(--light); stroke-width: 1.6; }
</style>
</head>
<body>

<section class="card front" aria-label="Frente do cartão">
  <div class="identity">
    <div class="monogram">RB</div>
    <div class="name">DR. RENATO BASTIANI</div>
    <div class="specialty">CIRURGIÃO PLÁSTICO</div>
  </div>
  <div class="socials">
    <div class="social"><span class="social-mark square"></span>DR.RENATOBASTIANI</div>
    <div class="social"><span class="social-mark circle"></span>@RENATO.BASTIANI.52</div>
    <div class="social"><span class="social-mark circle"></span>CLINICABASTIANI.COM.BR</div>
  </div>
</section>

<section class="card back" aria-label="Verso do cartão">
  <div class="header">
    <div class="monogram">RB</div>
    <div>
      <div class="name">DR. RENATO BASTIANI</div>
      <div class="specialty">CIRURGIÃO PLÁSTICO</div>
    </div>
  </div>
  <div class="registration">CRM 507 219</div>
  <div class="band">
    <div class="address">
      <div class="line">
        <svg class="icon" viewBox="0 0 16 16"><path d="M8 15s-5-5.2-5-8.7A5 5 0 0 1 13 6.3C13 9.8 8 15 8 15z"/><circle cx="8" cy="6.3" r="1.8"/></svg>
        Av Dr Teixeira Lopes, 2710, sala 305 - Vila Olímpia
      </div>
      <div class="line">São Paulo/SP</div>
      <div class="line">
        <svg class="icon" viewBox="0 0 16 16"><path d="M4 1.5l2.3 3-1.4 1.6a8 8 0 0 0 5 5l1.6-1.4 3 2.3-1.3 2.3C8 14 2 8 1.7 2.8z"/></svg>
        11 4172-5036
      </div>
    </div>
    <div class="address">
      <div class="line">
        <svg class="icon" viewBox="0 0 16 16"><path d="M8 15s-5-5.2-5-8.7A5 5 0 0 1 13 6.3C13 9.8 8 15 8 15z"/><circle cx="8" cy="6.3" r="1.8"/></svg>
        Al. Itapeva, 47, 3 andar - Alphaville
      </div>
      <div class="line">Barueri/SP</div>
      <div class="line">
        <svg class="icon" viewBox="0 0 16 16"><path d="M4 1.5l2.3 3-1.4 1.6a8 8 0 0 0 5 5l1.6-1.4 3 2.3-1.3 2.3C8 14 2 8 1.7 2.8z"/></svg>
        11 6350-2481
      </div>
    </div>
  </div>
</section>

</body>
</html>
```